Modern Innovative Business Card Design

We require a nice, modern, clean business card design, ready for upload to Cardomora. Our company develops online banking software solutions for small financial insitutions. The design should be clean, professional, but yet not "corporate boring". See www.fyrolt.com for an idea of business image and profile. The design should communicate innovation, be modern and fresh, yet look professional and established.

Target Market(s)

Finance industry, bankers, entrepreneurs

Industry/Entity Type

Financial

Contact Information for Business Card

Tobias Wendlerup
CEO

FYROLT BV
Lindenwerf 38
1027 HX Amsterdam
The Netherlands

Phone: +31 20 517 8036
Direct: +31 20 604 1758
Skype: tobias.fyrolt
ceo@fyrolt.com
www.fyrolt.com

Font styles to use
Sans Serif

Requirements
Must have
• Should look clean, modern and professional. File should be ready for upload to cardomora.
Should not have
• Boring standard corporate layout

```html
<!DOCTYPE html>
<html lang="en">
<head>
<meta charset="utf-8">
<title>FYROLT Business Card</title>
<link href="https://fonts.googleapis.com/css2?family=Questrial&family=Montserrat:wght@700&display=swap" rel="stylesheet">
<style>
  :root {
    --bg: #d9d8d4;
    --charcoal: #4b4b4b;
    --charcoal-deep: #3c3c3c;
    --lime: #8cc21f;
    --lime-dark: #6fa00f;
    --ink: #3a3a3a;
    --ink-soft: #555;
    --rule: #b8b8b8;
    --paper: #ffffff;
    --chip-blue: #2a9fd8;
  }
  * { margin: 0; padding: 0; box-sizing: border-box; }
  html, body { width: 1200px; height: 871px; overflow: hidden; }
  body {
    background: var(--bg);
    position: relative;
    font-family: "Questrial", "Century Gothic", sans-serif;
    color: var(--ink);
  }

  .card {
    position: absolute;
    width: 540px;
    height: 310px;
    overflow: hidden;
    box-shadow: 0 10px 28px rgba(0,0,0,0.22);
  }

  /* Back side */
  .card-back {
    left: 70px; top: 90px;
    background: linear-gradient(160deg, var(--charcoal) 0%, var(--charcoal-deep) 100%);
  }
  .card-back .brand {
    position: absolute; left: 0; right: 0; top: 92px;
    display: flex; justify-content: center; align-items: center; gap: 14px;
  }
  .brand-square { width: 22px; height: 22px; background: var(--lime); }
  .card-back .brand-name {
    font-size: 60px; letter-spacing: 3px; color: #f2f2f2; line-height: 1;
  }
  .card-back .links {
    position: absolute; left: 0; right: 0; top: 204px;
    display: flex; justify-content: center; gap: 48px;
    font-size: 15px; color: #e6e6e6; letter-spacing: 0.5px;
  }
  .link { display: flex; align-items: center; gap: 8px; }
  .dot { width: 14px; height: 14px; border-radius: 50%; }
  .dot-web { background: var(--lime); }
  .dot-chat { background: var(--chip-blue); }
  .card-back .band {
    position: absolute; left: 0; right: 0; top: 236px; height: 36px;
    background: var(--lime);
  }

  /* Front side */
  .card-front {
    left: 590px; top: 470px;
    background: linear-gradient(135deg, #f4f4f4 0%, var(--paper) 55%);
  }
  .card-front .brand {
    position: absolute; right: 42px; top: 40px;
    display: flex; align-items: center; gap: 10px;
  }
  .card-front .brand-square { width: 16px; height: 16px; }
  .card-front .brand-name {
    font-size: 40px; letter-spacing: 2px; color: var(--ink-soft); line-height: 1;
  }
  .person { position: absolute; left: 40px; top: 62px; }
  .person-name {
    font-family: "Montserrat", sans-serif; font-weight: 700;
    font-size: 17px; color: var(--ink);
  }
  .person-role { font-size: 13px; color: var(--lime); margin-top: 3px; }
  .rule-left {
    position: absolute; left: 40px; top: 112px; width: 260px; height: 1px;
    background: var(--rule);
  }
  .address {
    position: absolute; left: 40px; top: 124px;
    font-size: 14px; line-height: 1.55; color: var(--ink-soft);
  }
  .rule-right {
    position: absolute; left: 290px; right: 40px; top: 186px; height: 1px;
    background: var(--rule);
  }
  .contacts {
    position: absolute; right: 40px; top: 196px;
    list-style: none; font-size: 15px; line-height: 1.55; color: var(--ink);
  }
  .contacts li { display: flex; justify-content: flex-end; align-items: center; gap: 14px; }
  .contacts svg { width: 14px; height: 14px; }
  .footer {
    position: absolute; left: 0; right: 0; bottom: 0; height: 14px;
  }
</style>
</head>
<body>

  <section class="card card-back">
    <div class="brand">
      <span class="brand-square"></span>
      <span class="brand-name">FYROLT</span>
    </div>
    <div class="links">
      <span class="link"><span class="dot dot-web"></span>www.fyrolt.com</span>
      <span class="link"><span class="dot dot-chat"></span>tobias.fyrolt</span>
    </div>
    <div class="band"></div>
  </section>

  <section class="card card-front">
    <div class="brand">
      <span class="brand-square"></span>
      <span class="brand-name">FYROLT</span>
    </div>

    <div class="person">
      <div class="person-name">Tobias Wendlerup</div>
      <div class="person-role">CEO</div>
    </div>
    <div class="rule-left"></div>

    <address class="address" style="font-style:normal">
      FYROLT BV<br>
      Lindenwerf 38 1027 HX<br>
      Amsterdam The Netherlands
    </address>

    <div class="rule-right"></div>
    <ul class="contacts">
      <li>+31 20 517 8036
        <svg viewBox="0 0 16 16"><path d="M4 2h3l1 3-2 1.5a8 8 0 0 0 3.5 3.5L11 8l3 1v3a2 2 0 0 1-2 2A10 10 0 0 1 2 4a2 2 0 0 1 2-2z" fill="none" stroke="#8cc21f" stroke-width="1.4"/></svg>
      </li>
      <li>+31 20 604 1758
        <svg viewBox="0 0 16 16"><path d="M4 2h3l1 3-2 1.5a8 8 0 0 0 3.5 3.5L11 8l3 1v3a2 2 0 0 1-2 2A10 10 0 0 1 2 4a2 2 0 0 1 2-2z" fill="none" stroke="#8cc21f" stroke-width="1.4"/></svg>
      </li>
      <li>ceo@fyrolt.com
        <svg viewBox="0 0 16 16"><rect x="1.5" y="3.5" width="13" height="9" fill="none" stroke="#8cc21f" stroke-width="1.4"/><path d="M1.5 3.5 8 9l6.5-5.5" fill="none" stroke="#8cc21f" stroke-width="1.4"/></svg>
      </li>
    </ul>

    <svg class="footer" viewBox="0 0 540 14" preserveAspectRatio="none">
      <rect x="0" y="0" width="540" height="14" fill="#4b4b4b"/>
      <polygon points="340,0 520,0 540,14 355,14" fill="#8cc21f"/>
    </svg>
  </section>

</body>
</html>
```